Awesome Digital Ad Design – Pellucid Adreach

I am going to be setting up a Pellucid Adreach ad campaign I need creatives for.

Several sizes are needed in the end, however, please submit your design concept in the following 2 sizes to start:
Medium rectangle: 300X250
Leaderboard: 728X90

Original artwork/design files and images used expected upon payment and as part of the final delivery.

Ads should match our company brand and the information on this webpage: http://www.harborlyneworks.com/real-estate-marketing/
SEE MORE INSTRUCTIONS IN ATTACHED WORD DOC
Updates

Target Market(s)

Business-To-Business Audience –Real Estate Company Executives (Presidents/VPs/Owners/CEOs/Sales Managers).

Industry/Entity Type

Real Estate

Font styles to use
Sans Serif

Requirements
Must have
• Copy should be minimal words, billboard like. Please use real photos/images that would appeal to real estate high-level decision-maker executives.
Should not have
• No cartoons or graphics

```html
<!DOCTYPE html>
<html lang="en">
<head>
<meta charset="utf-8">
<title>Harborlyne Works – Display Ad Set</title>
<link rel="stylesheet" href="https://fonts.googleapis.com/css2?family=Oswald:wght@400;500&family=Open+Sans:wght@700;800&display=swap">
<style>
  :root {
    --page: #ffffff;
    --label: #333333;
    --frame: #6e2b3f;
    --gold: #8a7530;
    --maroon: #6e2b3f;
    --orange: #f26a1b;
    --tag-dark: #4e7390;
    --tag-light: #7896b0;
    --white: #ffffff;
    --brand-ink: #3a3a3a;
    --office-light: #eef3f4;
    --office-mid: #d6e0e3;
    --hair: rgba(120, 78, 52, 0.28);
    --skin: rgba(205, 160, 130, 0.22);
    --blazer: rgba(140, 138, 124, 0.55);
    --shirt: rgba(40, 40, 42, 0.35);
  }
  * { box-sizing: border-box; margin: 0; padding: 0; }
  html, body { width: 1200px; height: 1187px; overflow: hidden; background: var(--page); }
  .stage {
    position: relative; width: 900px; height: 890px;
    transform: scale(1.33333); transform-origin: 0 0;
  }
  .size-label {
    position: absolute; font-family: "Oswald", sans-serif; font-weight: 400;
    font-size: 14px; color: var(--label); letter-spacing: 0.2px;
  }
  .ad {
    position: absolute; overflow: hidden; border: 1px solid var(--frame);
    background: var(--office-light);
  }
  .photo { position: absolute; }
  .brand {
    position: absolute; font-family: "Open Sans", sans-serif; font-weight: 700;
    color: var(--brand-ink); line-height: 1.15;
  }
  .tag {
    position: absolute; font-family: "Oswald", sans-serif; color: var(--white);
    text-transform: uppercase; white-space: nowrap; line-height: 1;
    display: flex; align-items: center; padding: 0 4px;
  }
  .tag--top { background: var(--tag-dark); font-weight: 400; }
  .tag--main { background: var(--tag-light); font-weight: 500; letter-spacing: 0.5px; }
  .offer {
    position: absolute; background: var(--gold); color: var(--white);
    font-family: "Open Sans", sans-serif; font-weight: 700; text-align: center;
    display: flex; align-items: center; justify-content: center; letter-spacing: 0.3px;
  }
  .offer strong { font-weight: 800; }
  .action { position: absolute; background: var(--maroon); }
  .cta {
    position: absolute; background: var(--orange); color: var(--white);
    font-family: "Oswald", sans-serif; font-weight: 400; text-transform: uppercase;
    display: flex; align-items: center; justify-content: center; border-radius: 2px;
  }
</style>
</head>
<body>
<div class="stage">

  <span class="size-label" style="left:77px;top:40px;">300X250</span>
  <div class="ad ad--medium" style="left:77px;top:67px;width:300px;height:250px;">
    <div class="photo" role="img" aria-label="Smiling businesswoman with shoulder-length brown hair in a bright office"
         style="left:0;top:0;width:300px;height:176px;background:
           radial-gradient(ellipse 28% 45% at 80% 108%, var(--shirt), transparent 75%),
           radial-gradient(ellipse 40% 55% at 80% 112%, var(--blazer), transparent 75%),
           radial-gradient(ellipse 22% 38% at 78% 40%, var(--skin), transparent 75%),
           radial-gradient(ellipse 30% 55% at 78% 45%, var(--hair), transparent 75%),
           linear-gradient(90deg, var(--office-light) 0%, var(--office-mid) 100%);"></div>
    <div class="brand" style="left:9px;top:28px;font-size:8px;">Harborlyne<br>Works</div>
    <div class="tag tag--top" style="left:8px;top:99px;height:23px;font-size:18px;">Client Follow-Up</div>
    <div class="tag tag--main" style="left:8px;top:122px;height:33px;font-size:28.5px;">Made Simple</div>
    <div class="offer" style="left:0;top:175px;width:300px;height:34px;font-size:12.5px;">Virtually No Cost To Your Company!</div>
    <div class="action" style="left:0;top:209px;width:300px;height:41px;"></div>
    <div class="cta" style="left:60px;top:215px;width:180px;height:28px;font-size:16px;">Get Started Today!</div>
  </div>

  <span class="size-label" style="left:417px;top:40px;">300X600</span>
  <div class="ad ad--halfpage" style="left:417px;top:67px;width:300px;height:600px;">
    <div class="photo" role="img" aria-label="Portrait of a smiling businesswoman with wavy brown hair and a grey blazer"
         style="left:0;top:0;width:300px;height:471px;background:
           radial-gradient(ellipse 30% 22% at 62% 100%, var(--shirt), transparent 75%),
           radial-gradient(ellipse 60% 28% at 65% 104%, var(--blazer), transparent 75%),
           radial-gradient(ellipse 30% 24% at 58% 45%, var(--skin), transparent 75%),
           radial-gradient(ellipse 48% 40% at 60% 48%, var(--hair), transparent 75%),
           linear-gradient(160deg, var(--office-light) 0%, var(--office-mid) 100%);"></div>
    <div class="brand" style="left:18px;top:45px;font-size:10px;">Harborlyne<br>Works</div>
    <div class="tag tag--top" style="left:30px;top:368px;height:32px;font-size:26px;">Client Follow-Up</div>
    <div class="tag tag--main" style="left:30px;top:400px;height:47px;font-size:42px;">Made Simple</div>
    <div class="offer" style="left:0;top:470px;width:300px;height:70px;font-size:22px;line-height:1.1;">
      <span>Virtually <strong>NO COST</strong><br>To Your Company!</span>
    </div>
    <div class="action" style="left:0;top:540px;width:300px;height:60px;"></div>
    <div class="cta" style="left:33px;top:552px;width:234px;height:36px;font-size:20px;">Get Started Today!</div>
  </div>

  <span class="size-label" style="left:77px;top:700px;">728X90</span>
  <div class="ad ad--leaderboard" style="left:77px;top:727px;width:728px;height:90px;">
    <div class="photo" role="img" aria-label="Smiling businesswoman in a bright office setting"
         style="left:0;top:0;width:437px;height:90px;background:
           radial-gradient(ellipse 6% 40% at 84% 110%, var(--shirt), transparent 75%),
           radial-gradient(ellipse 12% 45% at 84% 115%, var(--blazer), transparent 75%),
           radial-gradient(ellipse 6% 38% at 83% 42%, var(--skin), transparent 75%),
           radial-gradient(ellipse 9% 60% at 83% 45%, var(--hair), transparent 75%),
           linear-gradient(90deg, var(--office-light) 0%, var(--office-mid) 100%);"></div>
    <div class="brand" style="left:14px;top:32px;font-size:8.5px;">Harborlyne<br>Works</div>
    <div class="tag tag--top" style="left:106px;top:12px;height:26px;font-size:21px;">Client Follow-Up</div>
    <div class="tag tag--main" style="left:106px;top:38px;height:40px;font-size:35px;">Made Simple</div>
    <div class="offer" style="left:437px;top:0;width:291px;height:45px;font-size:12.5px;">
      <span>Virtually <strong>NO COST</strong> To Your Company!</span>
    </div>
    <div class="action" style="left:437px;top:45px;width:291px;height:45px;"></div>
    <div class="cta" style="left:493px;top:54px;width:180px;height:28px;font-size:16px;">Get Started Today!</div>
  </div>

</div>
</body>
</html>
```